Zelvo - revolutionary mobile payment

The app is a P2P money trasfert, without the using of credit card or bank circuits it can transfer electronic money from one person to another consumers simply and immediatelly.
You can use the color you want, but the message we need to transert to consumer is simplicity, safety and coolness.
In attach the logo of the company and the wireframe of thre page of the app.
The goal is to design the page of the app with a clear, simple and intuitive graphic.
Updates

I have upgrade the brief with important information and detail, many thanks

Target Market(s)

all the people

Industry/Entity Type

Credit Card

Requirements
Must have
• You have to design one icon for each button in the first page, (shop is: where to shop)
in the second one a new intuitive image (instead of the hand) that let the user to understand that with a simple swipe he can process the payment
Nice to have
• You can include or esxclude what you want or belive can improve user experience of the app
Should not have
• too much color, too much button or information

```html
<!DOCTYPE html>
<html lang="en">
<head>
<meta charset="utf-8">
<title>Zelvo – mobile payment app screens</title>
<link href="https://fonts.googleapis.com/css2?family=Open+Sans:wght@400;600;700&family=Raleway:wght@300&display=swap" rel="stylesheet">
<style>
  :root {
    --navy: #1d3163;
    --navy-soft: #2c4280;
    --canvas: #e8efd9;
    --screen: #ffffff;
    --tile: #f4f4f4;
    --tile-border: #dcdcdc;
    --field-border: #9aa3b8;
    --text-grey: #5d6470;
    --intro-grey: #5b6470;
  }
  * { box-sizing: border-box; margin: 0; padding: 0; }
  html, body { width: 1200px; height: 1200px; overflow: hidden; }
  body {
    background: var(--canvas);
    position: relative;
    font-family: "Open Sans", sans-serif;
    color: var(--navy);
  }

  /* Brand header */
  .brand {
    position: absolute; left: 64px; top: 44px;
    display: flex; align-items: center; gap: 14px;
  }
  .brand-dot {
    width: 118px; height: 118px; border-radius: 50%;
    border: 12px solid var(--navy);
  }
  .brand-name {
    font-family: "Open Sans", sans-serif; font-weight: 700;
    font-size: 84px; line-height: 1; color: var(--navy); letter-spacing: 1px;
  }
  .intro {
    position: absolute; left: 76px; top: 182px; width: 540px;
    font-family: "Raleway", sans-serif; font-weight: 300;
    font-size: 19px; line-height: 26px; color: var(--intro-grey);
  }

  /* Screens */
  .screen {
    position: absolute; width: 256px; height: 455px;
    background: var(--screen); overflow: hidden;
    box-shadow: 0 2px 10px rgba(29, 49, 99, 0.15);
  }
  .screen--splash { left: 880px; top: 150px; }
  .screen--login { left: 67px; top: 560px; }
  .screen--home { left: 407px; top: 560px; background: var(--tile); }

  .inline-brand { display: flex; align-items: center; gap: 6px; }
  .inline-brand .dot { border-radius: 50%; border: 4px solid var(--navy); }
  .inline-brand .name { font-weight: 700; color: var(--navy); line-height: 1; }

  /* Splash */
  .splash-brand { position: absolute; left: 44px; top: 180px; }
  .splash-brand .dot { width: 44px; height: 44px; }
  .splash-brand .name { font-size: 32px; }
  .loader {
    position: absolute; left: 44px; top: 240px; width: 168px; height: 12px;
    border: 1px solid var(--navy);
  }
  .loader-fill { width: 62%; height: 100%; background: var(--navy); }
  .loader-label {
    position: absolute; left: 92px; top: 1px; font-size: 7px; color: var(--navy);
  }

  /* Login */
  .login-brand { position: absolute; left: 40px; top: 110px; }
  .login-brand .dot { width: 68px; height: 68px; border-width: 6px; }
  .login-brand .name { font-size: 46px; }
  .login-fields {
    position: absolute; left: 4px; top: 212px; width: 248px;
    border: 1px solid var(--field-border);
  }
  .login-field {
    height: 34px; padding-left: 23px; display: flex; align-items: center;
    font-size: 11px; font-weight: 600; color: var(--navy);
  }
  .login-field + .login-field { border-top: 1px solid var(--field-border); }
  .login-button {
    position: absolute; left: 4px; top: 294px; width: 248px; height: 34px;
    background: var(--navy); color: #fff; font-size: 12px; font-weight: 600;
    display: flex; align-items: center; justify-content: center;
  }
  .login-options {
    position: absolute; left: 0; right: 0; top: 340px;
    display: flex; justify-content: center; align-items: center; gap: 6px;
    font-size: 8px; color: var(--text-grey);
  }
  .login-options .link { text-decoration: underline; color: var(--navy); margin-left: 8px; }
  .signup {
    position: absolute; left: 0; right: 0; top: 422px;
    display: flex; justify-content: center; align-items: center; gap: 8px;
    font-size: 10px; color: var(--text-grey);
  }

  /* Home */
  .app-bar {
    height: 27px; background: var(--navy); display: flex; align-items: center;
    justify-content: space-between; padding: 0 8px;
  }
  .app-bar .inline-brand { margin-left: 6px; margin-right: auto; gap: 3px; }
  .app-bar .dot { width: 14px; height: 14px; border: 2px solid #fff; }
  .app-bar .name { color: #fff; font-size: 10px; }
  .profile { background: #fff; height: 123px; text-align: center; padding-top: 20px; }
  .avatar {
    width: 70px; height: 70px; border-radius: 50%; margin: 0 auto;
    background: linear-gradient(160deg, #c9ced6, #8a8f9a);
  }
  .profile-name { font-size: 11px; color: var(--text-grey); margin-top: 8px; }
  .tiles {
    display: grid; grid-template-columns: 114px 114px; gap: 6px 6px;
    padding: 18px 0 0 12px;
  }
  .tile {
    height: 111px; background: var(--tile); border: 1px solid var(--tile-border);
    display: flex; flex-direction: column; align-items: center; justify-content: center; gap: 8px;
    font-size: 13px; color: var(--navy);
  }
  .tile svg { width: 36px; height: 40px; }
</style>
</head>
<body>

  <header class="brand">
    <div class="brand-dot"></div>
    <div class="brand-name">Zelvo</div>
  </header>
  <p class="intro">The app is a P2P money trasfert, without the using of credit card or bank circuits it can transfer electronic money from one person to another consumers simply and immediatelly.</p>

  <!-- Splash screen -->
  <section class="screen screen--splash">
    <div class="inline-brand splash-brand"><span class="dot"></span><span class="name">Zelvo</span></div>
    <div class="loader"><div class="loader-fill"></div><span class="loader-label">Loading...</span></div>
  </section>

  <!-- Login screen -->
  <section class="screen screen--login">
    <div class="inline-brand login-brand"><span class="dot"></span><span class="name">Zelvo</span></div>
    <div class="login-fields">
      <div class="login-field">Username:</div>
      <div class="login-field">Password:</div>
    </div>
    <div class="login-button">Log in</div>
    <div class="login-options">
      <span>Remember me</span>
      <svg width="11" height="11" viewBox="0 0 12 12"><circle cx="6" cy="6" r="5" fill="none" stroke="#1d3163"/><path d="M3.5 6.2l1.7 1.6 3.3-3.4" fill="none" stroke="#1d3163" stroke-width="1.2"/></svg>
      <span class="link">Forgot password?</span>
    </div>
    <div class="signup">
      <span>Don't have an account?</span>
      <svg width="18" height="18" viewBox="0 0 18 18"><circle cx="9" cy="9" r="8" fill="none" stroke="#1d3163"/><path d="M9 5v8M5 9h8" stroke="#1d3163" stroke-width="1.2"/></svg>
    </div>
  </section>

  <!-- Home screen -->
  <section class="screen screen--home">
    <div class="app-bar">
      <svg width="8" height="12" viewBox="0 0 8 12"><path d="M6 1L1.5 6 6 11" fill="none" stroke="#fff" stroke-width="1.5"/></svg>
      <div class="inline-brand"><span class="dot"></span><span class="name">Zelvo</span></div>
      <svg width="12" height="10" viewBox="0 0 12 10"><path d="M0 1h12M0 5h12M0 9h12" stroke="#fff" stroke-width="1.6"/></svg>
    </div>
    <div class="profile">
      <div class="avatar" role="img" aria-label="Profile photo of the account holder"></div>
      <div class="profile-name">Daniel Marsh</div>
    </div>
    <div class="tiles">
      <div class="tile">
        <svg viewBox="0 0 36 40"><rect x="6" y="8" width="22" height="14" rx="2" fill="#1d3163" transform="rotate(-25 17 15)"/><circle cx="17" cy="15" r="3.5" fill="#fff"/><path d="M6 36c4-8 10-10 16-8l8-4" fill="none" stroke="#1d3163" stroke-width="3" stroke-linecap="round"/></svg>
        <span>Pay</span>
      </div>
      <div class="tile">
        <svg viewBox="0 0 36 40"><path d="M18 3l14 5v11c0 9-6 15-14 19C10 34 4 28 4 19V8z" fill="#1d3163"/><path d="M14 15a4 4 0 1 1 6 3.5c-1.5.8-2 1.6-2 3.5" fill="none" stroke="#fff" stroke-width="2.4"/><circle cx="18" cy="27" r="1.7" fill="#fff"/></svg>
        <span>Ask</span>
      </div>
      <div class="tile">
        <svg viewBox="0 0 36 40"><path d="M12 4l6 4 6-4-3 8h-6z" fill="#1d3163"/><path d="M14 13h8c8 6 11 13 9 19-1 4-5 6-13 6S6 36 5 32c-2-6 1-13 9-19z" fill="#1d3163"/><text x="18" y="31" font-family="Open Sans, sans-serif" font-size="13" font-weight="700" fill="#fff" text-anchor="middle">$</text></svg>
        <span>Account</span>
      </div>
      <div class="tile">
        <svg viewBox="0 0 40 40"><path d="M2 16l11-4 13 4 12-4v24l-12 4-13-4-11 4z" fill="none" stroke="#1d3163" stroke-width="1.8"/><path d="M13 12v24M26 16v24" stroke="#1d3163" stroke-width="1.5"/><path d="M20 2a7 7 0 0 1 7 7c0 5-7 12-7 12s-7-7-7-12a7 7 0 0 1 7-7z" fill="#fff" stroke="#1d3163" stroke-width="2.5"/><circle cx="20" cy="9" r="2.4" fill="#1d3163"/></svg>
        <span>Shop</span>
      </div>
    </div>
  </section>

</body>
</html>
```